Design Catagory App Icons for Brevlo.com new app launching in 2020

We need the icons designed for our categories in our app that suit the colors and layout of the app. 20 icons that need doing for an APP menu see on the left of the image I have uploaded. On or the sliding menu on the left we have small icons that represent the master categories. The master categories are listed in column A in the spreadsheet provided and we need an icon for each category that would sit above the words and suit the apps design and flow and colors.

Target Market(s)

Men all ages

Industry/Entity Type

Retail

Requirements
Must have
• An icon for each category listed in the spreadsheet to be successful.
Nice to have
• All the icons work together in the same family
Should not have
• Don't combine too many colors

```html
<!DOCTYPE html>
<html lang="en">
<head>
<meta charset="utf-8">
<title>Brevlo.com – Category Menu Icons</title>
<link rel="stylesheet" href="https://fonts.googleapis.com/css2?family=Barlow:wght@400;500;600;700;800&display=swap">
<style>
  :root {
    --canvas-bg: #e4e6e8;
    --app-dark: #2e2f31;
    --app-white: #ffffff;
    --menu-blue: #1a7fe8;
    --menu-blue-band: #4a9ff2;
    --menu-grey-band: #dedede;
    --menu-text: #2b2b2b;
    --price-red: #c8102e;
    --muted: #8a8a8a;
    --ink: #1e1e1e;
  }
  html, body { margin: 0; padding: 0; width: 1200px; height: 1200px; overflow: hidden; background: var(--canvas-bg); }
  .artboard { display: block; width: 1200px; height: 1200px; }
  .ui-text { font-family: "Barlow", sans-serif; }
  .status-time { font-weight: 700; font-size: 13px; fill: var(--app-white); }
  .search-hint { font-weight: 500; font-size: 7.5px; fill: #555; letter-spacing: .3px; }
  .section-title { font-weight: 800; font-size: 13px; fill: var(--ink); }
  .see-all { font-weight: 700; font-size: 6.5px; fill: var(--ink); }
  .product-name { font-weight: 700; font-size: 7px; fill: var(--ink); }
  .price { font-weight: 700; font-size: 9.5px; fill: var(--price-red); }
  .price-small { font-weight: 700; font-size: 7.5px; fill: var(--price-red); }
  .price-old { font-weight: 500; font-size: 8.5px; fill: var(--muted); text-decoration: line-through; }
  .price-old-small { font-weight: 500; font-size: 6px; fill: var(--muted); text-decoration: line-through; }
  .banner-title { font-weight: 800; font-size: 40px; fill: var(--app-white); letter-spacing: -1px; }
  .banner-hint { font-weight: 600; font-size: 6.5px; fill: var(--app-white); }
  .filters-label { font-weight: 700; font-size: 8px; fill: var(--app-white); letter-spacing: .4px; }
  .nav-label { font-weight: 600; font-size: 6.5px; fill: #9a9a9a; letter-spacing: .3px; }
  .nav-label.is-active { fill: var(--app-white); }
  .menu-label-sm { font-weight: 500; font-size: 6.3px; fill: var(--menu-text); }
  .menu-label-sm.on-blue { fill: var(--app-white); }
  .menu-label-lg { font-weight: 500; font-size: 12.5px; fill: var(--menu-text); letter-spacing: .2px; }
  .menu-label-lg.on-blue { fill: var(--app-white); }
  .icon-line { fill: none; stroke: var(--app-white); stroke-width: 2; stroke-linecap: round; stroke-linejoin: round; }
  .nav-icon { fill: none; stroke: #9a9a9a; stroke-width: 1.6; stroke-linecap: round; stroke-linejoin: round; }
  .nav-icon.is-active { stroke: var(--app-white); }
</style>
</head>
<body>
<svg class="artboard ui-text" viewBox="0 0 1200 1200" xmlns="http://www.w3.org/2000/svg">
  <defs>
    <linearGradient id="menuGrey" x1="0" y1="0" x2="0" y2="1">
      <stop offset="0" stop-color="#d6d6d6"/>
      <stop offset="1" stop-color="#a8a8a8"/>
    </linearGradient>
    <linearGradient id="bannerTone" x1="0" y1="0" x2="1" y2="1">
      <stop offset="0" stop-color="#5a1614"/>
      <stop offset=".55" stop-color="#2a1210"/>
      <stop offset="1" stop-color="#140c0b"/>
    </linearGradient>
    <linearGradient id="redDrill" x1="0" y1="0" x2="0" y2="1">
      <stop offset="0" stop-color="#f2f2f2"/><stop offset=".5" stop-color="#d8473f"/><stop offset="1" stop-color="#f4f4f4"/>
    </linearGradient>
    <linearGradient id="yellowDrill" x1="0" y1="0" x2="0" y2="1">
      <stop offset="0" stop-color="#f4f4f4"/><stop offset=".5" stop-color="#e7b52c"/><stop offset="1" stop-color="#f4f4f4"/>
    </linearGradient>
    <linearGradient id="tealDrill" x1="0" y1="0" x2="0" y2="1">
      <stop offset="0" stop-color="#f4f4f4"/><stop offset=".5" stop-color="#2b6f7c"/><stop offset="1" stop-color="#f4f4f4"/>
    </linearGradient>
    <linearGradient id="darkDrill" x1="0" y1="0" x2="0" y2="1">
      <stop offset="0" stop-color="#f4f4f4"/><stop offset=".5" stop-color="#2a2a2a"/><stop offset="1" stop-color="#f4f4f4"/>
    </linearGradient>
    <clipPath id="screenClip" clipPathUnits="userSpaceOnUse">
      <rect x="65" y="52" width="328" height="712" rx="28"/>
    </clipPath>
    <filter id="stripShadow" x="-20%" y="-5%" width="150%" height="115%">
      <feDropShadow dx="6" dy="8" stdDeviation="8" flood-color="#000" flood-opacity=".25"/>
    </filter>

    <!-- category icons -->
    <symbol id="ico-featured" viewBox="0 0 48 48"><g class="icon-line"><rect x="8" y="8" width="32" height="28" rx="2"/><path d="M8 14h32M12 11h1M15 11h1M24 16v3M24 31v3M15 25h3M30 25h3M6 40h36"/><circle cx="24" cy="25" r="6"/><circle cx="24" cy="25" r="2"/></g></symbol>
    <symbol id="ico-powertools" viewBox="0 0 48 48"><g class="icon-line"><path d="M14 10h20a4 4 0 0 1 4 4v6a4 4 0 0 1-4 4h-6l-2 12h6v4H18v-4h2l2-12h-8z"/><path d="M14 14H8M14 20H8M4 17h4"/><circle cx="30" cy="17" r="3"/></g></symbol>
    <symbol id="ico-accessories" viewBox="0 0 48 48"><g class="icon-line"><path d="M12 8v32M18 12v28M24 10v30M30 8v32M36 10v30"/><path d="M28 14l4 2-4 2 4 2-4 2 4 2M34 16l4 2-4 2 4 2-4 2 4 2"/></g></symbol>
    <symbol id="ico-bench" viewBox="0 0 48 48"><g class="icon-line"><path d="M10 8v30M10 10h26v6H16M10 24h28v6H10M24 30v10M18 40h12M16 16v8"/></g></symbol>
    <symbol id="ico-outdoor" viewBox="0 0 48 48"><g class="icon-line"><path d="M8 6l10 22M12 18h4"/><rect x="16" y="28" width="24" height="8" rx="3"/><circle cx="18" cy="38" r="4"/><circle cx="38" cy="38" r="4"/></g></symbol>
    <symbol id="ico-power" viewBox="0 0 48 48"><g class="icon-line"><path d="M18 20a6 6 0 1 1 12 0c0 3-3 5-3 8h-6c0-3-3-5-3-8z"/><path d="M21 31h6M24 31v10M24 38c-4-4-9-3-12-1 4 3 9 3 12 1zM24 36c4-4 9-3 12-1-4 3-9 3-12 1zM16 42h16M10 12l3 2M38 12l-3 2M24 4v3"/></g></symbol>
    <symbol id="ico-handtools" viewBox="0 0 48 48"><g class="icon-line"><path d="M10 12a6 6 0 0 0 8 8l18 18a3 3 0 0 0 4-4L22 16a6 6 0 0 0-8-8l4 4-2 4h-4z"/><path d="M34 8l6 6-4 4-6-6zM31 15L12 36l4 4 19-21"/></g></symbol>
    <symbol id="ico-auto" viewBox="0 0 48 48"><g class="icon-line"><path d="M8 30a10 10 0 0 1 20 0zM6 30h24M12 34h12v8H12z"/><path d="M34 6a5 5 0 0 0 0 9v18a5 5 0 0 0 0 9M40 6a5 5 0 0 1 0 9v18a5 5 0 0 1 0 9"/></g></symbol>
    <symbol id="ico-storage" viewBox="0 0 48 48"><g class="icon-line"><rect x="6" y="16" width="36" height="24" rx="2"/><path d="M18 16v-6h12v6M6 24h36M19 29l10 8M29 29l-10 8"/></g></symbol>
    <symbol id="ico-inspection" viewBox="0 0 48 48"><g class="icon-line"><circle cx="18" cy="22" r="12"/><circle cx="18" cy="22" r="5"/><path d="M18 34h24v-6H28M34 34v-3M38 34v-3"/></g></symbol>
    <symbol id="ico-cleaning" viewBox="0 0 48 48"><g class="icon-line"><path d="M10 22h22l-3 20H13zM16 10h6v12h-6zM22 12l5-2M28 22V12h6v10M30 12V8h4"/><circle cx="38" cy="38" r="4"/><circle cx="32" cy="41" r="3"/></g></symbol>
    <symbol id="ico-safety" viewBox="0 0 48 48"><g class="icon-line"><path d="M14 16a10 10 0 0 1 20 0zM11 16h26M24 6v10M12 44V32l8-6 4 6 4-6 8 6v12M24 32v12M16 38h4M28 38h4"/></g></symbol>
    <symbol id="ico-farm" viewBox="0 0 48 48"><g class="icon-line"><rect x="8" y="22" width="22" height="10"/><path d="M12 22V12h12v10M30 26h8v6M36 26v-6M38 8a6 6 0 0 1 4 4M38 4a10 10 0 0 1 8 8"/><circle cx="14" cy="36" r="6"/><circle cx="36" cy="38" r="4"/></g></symbol>
    <symbol id="ico-vintage" viewBox="0 0 48 48"><g class="icon-line"><path d="M6 30l20-8 16 6-20 8zM6 30v6l16 6 20-8v-6M10 34l12 4M28 22l8-12M34 6l6 4-3 4-6-4z"/></g></symbol>
    <symbol id="ico-refurbished" viewBox="0 0 48 48"><g class="icon-line"><path d="M24 6v6M24 36v6M6 24h6M36 24h6M11 11l4 4M33 33l4 4M11 37l4-4M33 15l4-4M18 30l10-10M28 16a4 4 0 0 0 4 4"/><circle cx="24" cy="24" r="12"/></g></symbol>
    <symbol id="ico-preowned" viewBox="0 0 48 48"><g class="icon-line"><rect x="12" y="6" width="24" height="20" rx="2"/><path d="M12 11h24"/><circle cx="24" cy="19" r="4"/><path d="M6 36h8l6-3h10a2 2 0 0 1 0 4h-8M30 37l10-8a2 2 0 0 1 2 3L32 42H6"/></g></symbol>
    <symbol id="ico-spare" viewBox="0 0 48 48"><g class="icon-line"><rect x="12" y="16" width="24" height="18" rx="2"/><path d="M16 16v-4h8v4M6 22h6v6H6M36 22h6v6h-6M16 34v6h16v-6M16 21h16M16 25h16M16 29h16"/></g></symbol>

    <!-- shared shop screen (header, content, navigation) -->
    <g id="shopScreen">
      <rect class="screen-bg" x="65" y="52" width="328" height="712" fill="var(--app-white)"/>
      <rect class="app-header" x="65" y="52" width="328" height="70" fill="var(--app-dark)"/>
      <text class="status-time" x="93" y="76">9:41</text>
      <g class="status-icons" fill="var(--app-white)">
        <rect x="324" y="71" width="2" height="3"/><rect x="327.5" y="69" width="2" height="5"/><rect x="331" y="67" width="2" height="7"/><rect x="334.5" y="65" width="2" height="9"/>
        <path d="M340 68a7 7 0 0 1 10 0l-1.5 1.5a5 5 0 0 0-7 0zM342.5 70.5a3.5 3.5 0 0 1 5 0L345 73z"/>
        <rect x="355" y="66" width="16" height="8" rx="2"/>
      </g>
      <rect class="search-bar" x="82" y="89" width="220" height="20" rx="10" fill="#e9e9e9"/>
      <circle cx="96" cy="98" r="4" fill="none" stroke="#555" stroke-width="1.5"/><path d="M99 101l3 3" stroke="#555" stroke-width="1.5"/>
      <text class="search-hint" x="112" y="102">SEARCH</text>
      <path class="share-icon" d="M330 106c2-7 7-10 13-10v-4l7 7-7 7v-4c-6 0-10 1-13 4z" fill="#eee"/>
      <g class="cart-icon" fill="none" stroke="#eee" stroke-width="2"><path d="M361 90h3l3 11h10l2-8h-14"/><circle cx="368" cy="105" r="1.5" fill="#eee"/><circle cx="376" cy="105" r="1.5" fill="#eee"/></g>

      <text class="section-title" x="153" y="155">TOOL OF THE DAY</text>
      <rect x="144" y="166" width="244" height="153" rx="3" fill="url(#bannerTone)" role="img" aria-label="Tool of the day photo: red cordless drill in a workshop"/>
      <text class="banner-title" x="189" y="238">TOOL OF</text>
      <text class="banner-title" x="195" y="278">THE DAY</text>
      <circle cx="252" cy="306" r="3" fill="#fff"/><circle cx="262" cy="306" r="2" fill="#888"/><circle cx="271" cy="306" r="2" fill="#888"/><circle cx="280" cy="306" r="2" fill="#888"/>
      <text class="banner-hint" x="311" y="309">SWIPE FOR MORE</text>

      <text class="section-title" x="153" y="349">WEEKLY TOP TEN</text>
      <rect x="325" y="337" width="52" height="15" rx="4" fill="none" stroke="#333" stroke-width="1"/>
      <text class="see-all" x="338" y="347">SEE ALL</text>

      <g class="product-card">
        <rect x="144" y="363" width="104" height="160" rx="3" fill="#fff" stroke="#ddd"/>
        <rect x="152" y="370" width="88" height="92" fill="url(#redDrill)" role="img" aria-label="Red cordless drill/driver kit"/>
        <rect x="231" y="368" width="12" height="12" rx="3" fill="#666"/>
        <text class="product-name" x="151" y="479">Forgeline F18 Cordless</text>
        <text class="product-name" x="151" y="488">Brushless 1/2 In. Drill/</text>
        <text class="product-name" x="151" y="497">Driver Kit</text>
        <text class="price" x="151" y="512">$89.00</text>
        <text class="price-old" x="191" y="512">$109.00</text>
      </g>
      <g class="product-card">
        <rect x="253" y="363" width="104" height="160" rx="3" fill="#fff" stroke="#ddd"/>
        <rect x="261" y="370" width="88" height="92" fill="url(#yellowDrill)" role="img" aria-label="Yellow cordless driver-drill"/>
        <rect x="340" y="368" width="12" height="12" rx="3" fill="#666"/>
        <text class="product-name" x="260" y="479">Kestrel Surge</text>
        <text class="product-name" x="260" y="488">Lithium-Ion 1/2 In.</text>
        <text class="product-name" x="260" y="497">Cordless Driver-Drill</text>
        <text class="price" x="260" y="512">$89.00</text>
      </g>
      <g class="product-card">
        <rect x="362" y="363" width="104" height="160" rx="3" fill="#fff" stroke="#ddd"/>
        <rect x="366" y="374" width="30" height="88" fill="url(#darkDrill)" role="img" aria-label="Black nail gun"/>
        <text class="product-name" x="368" y="479">Kestrel</text>
        <text class="product-name" x="368" y="488">Lithium</text>
        <text class="product-name" x="368" y="497">Cordless</text>
        <text class="price" x="368" y="512">$89.00</text>
      </g>

      <text class="section-title" x="153" y="553">JUST DROPPED</text>
      <rect x="325" y="541" width="52" height="15" rx="4" fill="none" stroke="#333" stroke-width="1"/>
      <text class="see-all" x="338" y="551">SEE ALL</text>

      <g class="mini-card"><rect x="144" y="566" width="78" height="77" rx="3" fill="#fff" stroke="#ddd"/><rect x="150" y="572" width="60" height="52" fill="url(#redDrill)" role="img" aria-label="Red compact screwdriver"/><rect x="207" y="571" width="10" height="10" rx="3" fill="#666"/><text class="price-small" x="150" y="639">$89.00</text><text class="price-old-small" x="180" y="639">$89.00</text></g>
      <g class="mini-card"><rect x="226" y="566" width="78" height="77" rx="3" fill="#fff" stroke="#ddd"/><rect x="232" y="572" width="60" height="52" fill="url(#yellowDrill)" role="img" aria-label="Yellow compact drill"/><rect x="289" y="571" width="10" height="10" rx="3" fill="#666"/><text class="price-small" x="231" y="639">$89.00</text></g>
      <g class="mini-card"><rect x="309" y="566" width="78" height="77" rx="3" fill="#fff" stroke="#ddd"/><rect x="315" y="572" width="60" height="52" fill="url(#tealDrill)" role="img" aria-label="Teal impact driver"/><rect x="372" y="571" width="10" height="10" rx="3" fill="#666"/><text class="price-small" x="313" y="639">$89.00</text></g>
      <g class="mini-card"><rect x="144" y="649" width="78" height="77" rx="3" fill="#fff" stroke="#ddd"/><rect x="150" y="655" width="60" height="52" fill="url(#yellowDrill)" role="img" aria-label="Yellow drill"/><rect x="207" y="654" width="10" height="10" rx="3" fill="#666"/></g>
      <g class="mini-card"><rect x="226" y="649" width="78" height="77" rx="3" fill="#fff" stroke="#ddd"/><rect x="232" y="655" width="60" height="52" fill="url(#tealDrill)" role="img" aria-label="Teal drill"/><rect x="289" y="654" width="10" height="10" rx="3" fill="#666"/></g>
      <g class="mini-card"><rect x="309" y="649" width="78" height="77" rx="3" fill="#fff" stroke="#ddd"/><rect x="315" y="655" width="60" height="52" fill="url(#redDrill)" role="img" aria-label="Red drill"/><rect x="372" y="654" width="10" height="10" rx="3" fill="#666"/></g>

      <g class="filters-pill">
        <rect x="200" y="673" width="78" height="22" rx="11" fill="#2e2f31" fill-opacity=".85"/>
        <path d="M211 680h9M212.5 684h6M214 688h3" stroke="#fff" stroke-width="1.4"/>
        <text class="filters-label" x="224" y="687">FILTERS</text>
      </g>
      <g class="chat-button">
        <circle cx="358" cy="676" r="20" fill="var(--menu-blue)"/>
        <rect x="349" y="668" width="18" height="14" rx="3" fill="#fff"/>
        <path d="M352 682l-2 4 6-4z" fill="#fff"/>
        <path d="M352 673h12M352 677h9" stroke="var(--menu-blue)" stroke-width="1.4"/>
      </g>

      <rect class="bottom-nav" x="65" y="705" width="328" height="59" fill="var(--app-dark)"/>
      <g class="nav-icon"><rect x="94" y="714" width="10" height="13" rx="1.5"/><path d="M98 712h8a1.5 1.5 0 0 1 1.5 1.5V725"/></g>
      <text class="nav-label" x="101" y="741" text-anchor="middle">HOME</text>
      <g class="nav-icon is-active"><circle cx="149" cy="719" r="5"/><path d="M153 723l4 4"/></g>
      <text class="nav-label is-active" x="151" y="741" text-anchor="middle">SHOP</text>
      <g class="nav-icon"><circle cx="195" cy="716" r="2.6"/><circle cx="204" cy="716" r="2.6"/><path d="M190 727a5 5 0 0 1 10 0zM199 727a5 5 0 0 1 10 0z"/></g>
      <text class="nav-label" x="199" y="741" text-anchor="middle">SOCIAL</text>
      <g class="nav-icon"><path d="M242 714l12 12M254 714l-12 12M240 716l4-4M252 728l4-4"/></g>
      <text class="nav-label" x="248" y="741" text-anchor="middle">SELLERS</text>
      <g class="nav-icon"><rect x="293" y="713" width="14" height="14" rx="3"/><path d="M300 716v8M296 720h8"/></g>
      <text class="nav-label" x="300" y="741" text-anchor="middle">ADD POST</text>
      <g class="nav-icon"><circle cx="356" cy="720" r="4"/><path d="M356 712v3M356 725v3M348 720h3M361 720h3M350.5 714.5l2 2M359.5 723.5l2 2M350.5 725.5l2-2M359.5 716.5l2-2"/></g>
      <text class="nav-label" x="356" y="741" text-anchor="middle">ACCOUNT</text>
      <rect class="home-indicator" x="171" y="753" width="120" height="4" rx="2" fill="#fff"/>
    </g>
  </defs>

  <rect class="canvas-bg" width="1200" height="1200" fill="var(--canvas-bg)"/>

  <!-- Phone screen: main categories menu -->
  <g class="phone-screen phone-screen--main" clip-path="url(#screenClip)">
    <use href="#shopScreen"/>
    <g class="side-menu">
      <path d="M65 122h90l-20 20v41H65z" fill="var(--menu-blue)"/>
      <path d="M126 131h10M126 131l4-3.5M126 131l4 3.5" class="icon-line" stroke-width="1.5"/>
      <rect x="65" y="169" width="70" height="14" fill="var(--menu-blue-band)"/>
      <use href="#ico-featured" x="84" y="128" width="32" height="32"/>
      <text class="menu-label-sm on-blue" x="100" y="179" text-anchor="middle">Featured</text>

      <rect x="65" y="183" width="70" height="52" fill="url(#menuGrey)"/><rect x="65" y="222" width="70" height="13" fill="var(--menu-grey-band)"/>
      <use href="#ico-powertools" x="86" y="186" width="30" height="30"/>
      <text class="menu-label-sm" x="100" y="231" text-anchor="middle">Powertools</text>

      <rect x="65" y="235" width="70" height="52" fill="url(#menuGrey)"/><rect x="65" y="270" width="70" height="17" fill="var(--menu-grey-band)"/>
      <use href="#ico-accessories" x="86" y="237" width="30" height="30"/>
      <text class="menu-label-sm" x="100" y="278" text-anchor="middle">Powertool</text>
      <text class="menu-label-sm" x="100" y="285" text-anchor="middle">Accessories</text>

      <rect x="65" y="287" width="70" height="52" fill="url(#menuGrey)"/><rect x="65" y="322" width="70" height="17" fill="var(--menu-grey-band)"/>
      <use href="#ico-bench" x="86" y="289" width="30" height="30"/>
      <text class="menu-label-sm" x="100" y="330" text-anchor="middle">Benchtools &amp;</text>
      <text class="menu-label-sm" x="100" y="337" text-anchor="middle">Woodworking</text>

      <rect x="65" y="339" width="70" height="53" fill="url(#menuGrey)"/><rect x="65" y="379" width="70" height="13" fill="var(--menu-grey-band)"/>
      <use href="#ico-outdoor" x="86" y="343" width="30" height="30"/>
      <text class="menu-label-sm" x="100" y="388" text-anchor="middle">Outdoor</text>

      <rect x="65" y="392" width="70" height="52" fill="var(--menu-blue)"/><rect x="65" y="431" width="70" height="13" fill="var(--menu-blue-band)"/>
      <use href="#ico-power" x="86" y="395" width="30" height="30"/>
      <text class="menu-label-sm on-blue" x="100" y="440" text-anchor="middle">Power &amp; Lighting</text>

      <rect x="65" y="444" width="70" height="52" fill="url(#menuGrey)"/><rect x="65" y="483" width="70" height="13" fill="var(--menu-grey-band)"/>
      <use href="#ico-handtools" x="86" y="447" width="30" height="30"/>
      <text class="menu-label-sm" x="100" y="492" text-anchor="middle">Handtools</text>

      <rect x="65" y="496" width="70" height="52" fill="url(#menuGrey)"/><rect x="65" y="535" width="70" height="13" fill="var(--menu-grey-band)"/>
      <use href="#ico-auto" x="86" y="499" width="30" height="30"/>
      <text class="menu-label-sm" x="100" y="544" text-anchor="middle">Auto &amp; Air Tools</text>

      <rect x="65" y="548" width="70" height="52" fill="url(#menuGrey)"/><rect x="65" y="587" width="70" height="13" fill="var(--menu-grey-band)"/>
      <use href="#ico-storage" x="86" y="551" width="30" height="30"/>
      <text class="menu-label-sm" x="100" y="596" text-anchor="middle">Storage &amp; Workshop</text>

      <rect x="65" y="600" width="70" height="53" fill="url(#menuGrey)"/><rect x="65" y="636" width="70" height="17" fill="var(--menu-grey-band)"/>
      <use href="#ico-inspection" x="86" y="603" width="30" height="30"/>
      <text class="menu-label-sm" x="100" y="644" text-anchor="middle">Inspection &amp;</text>
      <text class="menu-label-sm" x="100" y="651" text-anchor="middle">Measurement</text>

      <rect x="65" y="653" width="70" height="52" fill="var(--menu-blue)"/><rect x="65" y="692" width="70" height="13" fill="var(--menu-blue-band)"/>
      <use href="#ico-cleaning" x="86" y="656" width="30" height="30"/>
      <text class="menu-label-sm on-blue" x="100" y="701" text-anchor="middle">Cleaning Tools</text>
    </g>
  </g>

  <!-- Large strip: main categories -->
  <g class="category-strip category-strip--main" filter="url(#stripShadow)">
    <path d="M434 52h171l-39 48v66H434z" fill="var(--menu-blue)"/>
    <path d="M548 68h20M548 68l7-6M548 68l7 6" class="icon-line" stroke-width="2.4"/>
    <rect x="434" y="138" width="132" height="28" fill="var(--menu-blue-band)"/>
    <use href="#ico-featured" x="464" y="72" width="70" height="70"/>
    <text class="menu-label-lg on-blue" x="500" y="158" text-anchor="middle">Featured</text>

    <rect x="434" y="166" width="132" height="100" fill="url(#menuGrey)"/><rect x="434" y="237" width="132" height="29" fill="var(--menu-grey-band)"/>
    <use href="#ico-powertools" x="467" y="172" width="64" height="64"/>
    <text class="menu-label-lg" x="500" y="256" text-anchor="middle">Powertools</text>

    <rect x="434" y="266" width="132" height="98" fill="url(#menuGrey)"/><rect x="434" y="334" width="132" height="30" fill="var(--menu-grey-band)"/>
    <use href="#ico-accessories" x="470" y="270" width="60" height="60"/>
    <text class="menu-label-lg" x="500" y="347" text-anchor="middle">Powertool</text>
    <text class="menu-label-lg" x="500" y="360" text-anchor="middle">Accessories</text>

    <rect x="434" y="364" width="132" height="97" fill="url(#menuGrey)"/><rect x="434" y="431" width="132" height="30" fill="var(--menu-grey-band)"/>
    <use href="#ico-bench" x="470" y="368" width="60" height="60"/>
    <text class="menu-label-lg" x="500" y="444" text-anchor="middle">Benchtools &amp;</text>
    <text class="menu-label-lg" x="500" y="457" text-anchor="middle">Woodworking</text>

    <rect x="434" y="461" width="132" height="99" fill="url(#menuGrey)"/><rect x="434" y="531" width="132" height="29" fill="var(--menu-grey-band)"/>
    <use href="#ico-outdoor" x="470" y="467" width="60" height="60"/>
    <text class="menu-label-lg" x="500" y="550" text-anchor="middle">Outdoor</text>

    <rect x="434" y="560" width="132" height="97" fill="var(--menu-blue)"/><rect x="434" y="628" width="132" height="29" fill="var(--menu-blue-band)"/>
    <use href="#ico-power" x="470" y="565" width="60" height="60"/>
    <text class="menu-label-lg on-blue" x="500" y="647" text-anchor="middle">Power &amp; Lighting</text>

    <rect x="434" y="657" width="132" height="98" fill="url(#menuGrey)"/><rect x="434" y="726" width="132" height="29" fill="var(--menu-grey-band)"/>
    <use href="#ico-handtools" x="470" y="662" width="60" height="60"/>
    <text class="menu-label-lg" x="500" y="746" text-anchor="middle">Handtools</text>

    <rect x="434" y="755" width="132" height="98" fill="url(#menuGrey)"/><rect x="434" y="824" width="132" height="29" fill="var(--menu-grey-band)"/>
    <use href="#ico-auto" x="470" y="760" width="60" height="60"/>
    <text class="menu-label-lg" x="500" y="844" text-anchor="middle">Auto &amp; Air Tools</text>

    <rect x="434" y="853" width="132" height="98" fill="url(#menuGrey)"/><rect x="434" y="922" width="132" height="29" fill="var(--menu-grey-band)"/>
    <use href="#ico-storage" x="470" y="858" width="60" height="60"/>
    <text class="menu-label-lg" x="500" y="942" text-anchor="middle">Storage &amp; Workshop</text>

    <rect x="434" y="951" width="132" height="98" fill="url(#menuGrey)"/><rect x="434" y="1019" width="132" height="30" fill="var(--menu-grey-band)"/>
    <use href="#ico-inspection" x="470" y="955" width="60" height="60"/>
    <text class="menu-label-lg" x="500" y="1032" text-anchor="middle">Inspection &amp;</text>
    <text class="menu-label-lg" x="500" y="1045" text-anchor="middle">Measurement</text>

    <rect x="434" y="1049" width="132" height="99" fill="var(--menu-blue)"/><rect x="434" y="1119" width="132" height="29" fill="var(--menu-blue-band)"/>
    <use href="#ico-cleaning" x="470" y="1055" width="60" height="60"/>
    <text class="menu-label-lg on-blue" x="500" y="1139" text-anchor="middle">Cleaning Tools</text>
  </g>

  <!-- Large strip: secondary categories -->
  <g class="category-strip category-strip--secondary" filter="url(#stripShadow)">
    <path d="M593 191h172l-40 49v66H593z" fill="var(--menu-blue)"/>
    <path d="M706 207h20M706 207l7-6M706 207l7 6" class="icon-line" stroke-width="2.4"/>
    <rect x="593" y="278" width="132" height="28" fill="var(--menu-blue-band)"/>
    <use href="#ico-safety" x="626" y="208" width="64" height="64"/>
    <text class="menu-label-lg on-blue" x="659" y="297" text-anchor="middle">Safety &amp; Workwear</text>

    <rect x="593" y="306" width="132" height="98" fill="url(#menuGrey)"/><rect x="593" y="374" width="132" height="30" fill="var(--menu-grey-band)"/>
    <use href="#ico-farm" x="629" y="311" width="60" height="60"/>
    <text class="menu-label-lg" x="659" y="387" text-anchor="middle">Farm &amp; Industrial</text>
    <text class="menu-label-lg" x="659" y="400" text-anchor="middle">Equipment</text>

    <rect x="593" y="404" width="132" height="98" fill="url(#menuGrey)"/><rect x="593" y="473" width="132" height="29" fill="var(--menu-grey-band)"/>
    <use href="#ico-vintage" x="629" y="409" width="60" height="60"/>
    <text class="menu-label-lg" x="659" y="492" text-anchor="middle">Vintage Tools</text>

    <rect x="593" y="502" width="132" height="98" fill="url(#menuGrey)"/><rect x="593" y="571" width="132" height="29" fill="var(--menu-grey-band)"/>
    <use href="#ico-refurbished" x="629" y="507" width="60" height="60"/>
    <text class="menu-label-lg" x="659" y="590" text-anchor="middle">Refurbished</text>

    <rect x="593" y="600" width="132" height="98" fill="url(#menuGrey)"/><rect x="593" y="669" width="132" height="29" fill="var(--menu-grey-band)"/>
    <use href="#ico-preowned" x="629" y="605" width="60" height="60"/>
    <text class="menu-label-lg" x="659" y="688" text-anchor="middle">Preowned</text>

    <rect x="593" y="698" width="132" height="98" fill="var(--menu-blue)"/><rect x="593" y="767" width="132" height="29" fill="var(--menu-blue-band)"/>
    <use href="#ico-spare" x="629" y="703" width="60" height="60"/>
    <text class="menu-label-lg on-blue" x="659" y="786" text-anchor="middle">Spare Parts</text>
  </g>

  <!-- Phone screen: secondary categories menu -->
  <g class="phone-screen phone-screen--secondary" transform="translate(701 383)">
    <g clip-path="url(#screenClip)">
      <use href="#shopScreen"/>
      <g class="side-menu">
        <path d="M65 122h90l-20 20v41H65z" fill="var(--menu-blue)"/>
        <path d="M126 131h10M126 131l4-3.5M126 131l4 3.5" class="icon-line" stroke-width="1.5"/>
        <rect x="65" y="169" width="70" height="14" fill="var(--menu-blue-band)"/>
        <use href="#ico-safety" x="84" y="130" width="32" height="32"/>
        <text class="menu-label-sm on-blue" x="100" y="179" text-anchor="middle">Safety &amp; Workwear</text>

        <rect x="65" y="183" width="70" height="52" fill="url(#menuGrey)"/><rect x="65" y="218" width="70" height="17" fill="var(--menu-grey-band)"/>
        <use href="#ico-farm" x="86" y="185" width="30" height="30"/>
        <text class="menu-label-sm" x="100" y="226" text-anchor="middle">Farm &amp; Industrial</text>
        <text class="menu-label-sm" x="100" y="233" text-anchor="middle">Equipment</text>

        <rect x="65" y="235" width="70" height="52" fill="url(#menuGrey)"/><rect x="65" y="274" width="70" height="13" fill="var(--menu-grey-band)"/>
        <use href="#ico-vintage" x="86" y="238" width="30" height="30"/>
        <text class="menu-label-sm" x="100" y="283" text-anchor="middle">Vintage Tools</text>

        <rect x="65" y="287" width="70" height="52" fill="url(#menuGrey)"/><rect x="65" y="326" width="70" height="13" fill="var(--menu-grey-band)"/>
        <use href="#ico-refurbished" x="86" y="290" width="30" height="30"/>
        <text class="menu-label-sm" x="100" y="335" text-anchor="middle">Refurbished</text>

        <rect x="65" y="339" width="70" height="53" fill="url(#menuGrey)"/><rect x="65" y="379" width="70" height="13" fill="var(--menu-grey-band)"/>
        <use href="#ico-preowned" x="86" y="343" width="30" height="30"/>
        <text class="menu-label-sm" x="100" y="388" text-anchor="middle">Preowned</text>

        <rect x="65" y="392" width="70" height="52" fill="var(--menu-blue)"/><rect x="65" y="431" width="70" height="13" fill="var(--menu-blue-band)"/>
        <use href="#ico-spare" x="86" y="395" width="30" height="30"/>
        <text class="menu-label-sm on-blue" x="100" y="440" text-anchor="middle">Spare Parts</text>

        <rect x="65" y="444" width="70" height="52" fill="url(#menuGrey)"/><rect x="65" y="483" width="70" height="13" fill="var(--menu-grey-band)"/>
        <rect x="65" y="496" width="70" height="52" fill="url(#menuGrey)"/><rect x="65" y="535" width="70" height="13" fill="var(--menu-grey-band)"/>
        <rect x="65" y="548" width="70" height="52" fill="url(#menuGrey)"/><rect x="65" y="587" width="70" height="13" fill="var(--menu-grey-band)"/>
        <rect x="65" y="600" width="70" height="53" fill="url(#menuGrey)"/><rect x="65" y="640" width="70" height="13" fill="var(--menu-grey-band)"/>
        <rect x="65" y="653" width="70" height="52" fill="url(#menuGrey)"/><rect x="65" y="692" width="70" height="13" fill="var(--menu-grey-band)"/>
      </g>
    </g>
  </g>
</svg>
</body>
</html>
```